marlowe charters

We provide boar charter for :Fishing/whale watching and diving in Sydney Harbour providing for 12 passengersI have yet to have web page made but want to make logo first then do web page later. So I want to be able to edit and add this site to card later

Contact Information for Business Card

Captain Glen (Skip) Wigellphone no 0457710098email awigell4@gmail.comCompany name Brightwater Voyages Pty Ltd in association with open reef cruises

Font styles to use
Serif

Requirements
Nice to have
• perhaps a photo of boat and some stick diagrams of fishing.whales and diviving

```html
<!DOCTYPE html>
<html lang="en">
<head>
<meta charset="utf-8">
<title>Brightwater Voyages – Business Card</title>
<link href="https://fonts.googleapis.com/css2?family=Libre+Baskerville:wght@400;700&display=swap" rel="stylesheet">
<style>
  :root {
    --ocean-blue: #2a55b8;
    --ocean-deep: #1f45a0;
    --card-white: #f7f7f8;
    --stage: #e6e8ec;
    --photo-sky: #eef1f5;
    --photo-hull: #c9d2dc;
  }
  * { margin: 0; padding: 0; box-sizing: border-box; }
  html, body { width: 1200px; height: 780px; overflow: hidden; }
  body {
    background: var(--stage);
    font-family: "Libre Baskerville", Georgia, serif;
    display: flex;
    align-items: center;
    justify-content: center;
    gap: 40px;
  }
  .card {
    position: relative;
    width: 540px;
    height: 310px;
    border-radius: 16px;
    background: var(--card-white);
    overflow: hidden;
    box-shadow: 0 6px 18px rgba(0,0,0,.15);
  }
  .card__wave { position: absolute; left: 0; bottom: 0; width: 100%; height: 100%; }

  .brand {
    position: absolute;
    display: flex;
    align-items: center;
    gap: 12px;
    color: var(--ocean-blue);
  }
  .brand__ring {
    width: 62px; height: 62px;
    border: 3px solid var(--ocean-blue);
    border-radius: 50%;
    flex: none;
  }
  .brand__name { font-size: 15px; line-height: 1.25; letter-spacing: .5px; text-transform: uppercase; }
  .brand__sub { display: block; font-size: 9px; letter-spacing: 1px; margin-top: 3px; }
  .brand__assoc {
    display: block;
    font-size: 8.5px;
    text-transform: none;
    letter-spacing: .3px;
    border-top: 1px solid var(--ocean-blue);
    padding-top: 4px;
    margin-top: 5px;
  }

  .card--front .brand { left: 28px; top: 72px; width: 250px; }
  .divider {
    position: absolute;
    left: 290px; top: 40px;
    width: 1px; height: 120px;
    background: var(--ocean-blue);
  }
  .holder {
    position: absolute;
    left: 312px; top: 40px;
    color: var(--ocean-blue);
  }
  .holder__name { font-size: 28px; font-weight: 700; margin-bottom: 18px; }
  .contact { list-style: none; font-size: 12.5px; }
  .contact li { display: flex; align-items: center; gap: 8px; margin-bottom: 8px; }
  .contact svg { width: 16px; height: 16px; flex: none; }

  .photo {
    position: absolute; inset: 0;
    background: linear-gradient(160deg, var(--photo-sky) 0%, #ffffff 45%, var(--photo-hull) 100%);
  }
  .card--back .brand {
    right: 24px; top: 22px;
    flex-direction: row-reverse;
    text-align: right;
  }
</style>
</head>
<body>
  <section class="card card--front" aria-label="Business card front">
    <svg class="card__wave" viewBox="0 0 540 310" preserveAspectRatio="none" aria-hidden="true">
      <path d="M0 232 C80 228 140 212 200 214 C260 216 290 245 350 238 C410 230 440 205 540 200 L540 310 L0 310 Z" fill="var(--ocean-blue)"/>
    </svg>
    <div class="brand">
      <span class="brand__ring" aria-hidden="true"></span>
      <p class="brand__name">Brightwater Voyages
        <span class="brand__sub">Pty Ltd</span>
        <span class="brand__assoc">in association with open reef cruises</span>
      </p>
    </div>
    <span class="divider" aria-hidden="true"></span>
    <div class="holder">
      <h1 class="holder__name">Ferrant</h1>
      <ul class="contact">
        <li>
          <svg viewBox="0 0 16 16" aria-hidden="true"><rect width="16" height="16" rx="3" fill="var(--ocean-blue)"/><path d="M4.5 3.5h2l1 2.5-1.3 1a6 6 0 0 0 2.8 2.8l1-1.3 2.5 1v2a1 1 0 0 1-1 1A8 8 0 0 1 3.5 4.5a1 1 0 0 1 1-1z" fill="#fff"/></svg>
          0462385147
        </li>
        <li>
          <svg viewBox="0 0 16 16" aria-hidden="true"><rect width="16" height="16" rx="3" fill="var(--ocean-blue)"/><rect x="3.5" y="5" width="9" height="6.5" fill="none" stroke="#fff" stroke-width="1.2"/><path d="M3.5 5l4.5 3.8L12.5 5" fill="none" stroke="#fff" stroke-width="1.2"/></svg>
          gferrant7@tidemail.net
        </li>
      </ul>
    </div>
  </section>

  <section class="card card--back" aria-label="Business card back">
    <div class="photo" role="img" aria-label="Photograph of the white charter boat moored at the marina"></div>
    <div class="brand">
      <span class="brand__ring" aria-hidden="true"></span>
      <p class="brand__name">Brightwater Voyages
        <span class="brand__sub">Pty Ltd</span>
      </p>
    </div>
  </section>
</body>
</html>
```